Banner Ad for Resume Services Website

The add is for this web site: www.BrightCareerPages.net

The site offers 4 different services:

- Resume Writing (by a Certified Professional Resume Writer)
- Resume Posting (posts your resume to 85 job sites)
- Resume Distribution (sends your resume to hundreds of recruiters)
- Resume Online website (created an online resume with a domain name to your name)

Colors to be used are Blue, Yellow, etc... please check the website for inspiration.

Check the web site to learn more.

Target Market(s)

Unemployed, Professionals who want to switch jobs, etc..

Industry/Entity Type

Requirements
Must have
• We definitely one this to be included on the banner:

"Free Resume Samples"

in order to attract clicks.
Nice to have
• Some of the words we suggest to include on the banner are:

"How Good is Your Resume? Ask a Professional !"

Should not have
• No animation !

Do not place the LOGO on the banner as our LOGO might change in the near future. If you already submitted a banner with the LOGO on it, you can replace it with any other graphic that has a Resume/Jobs/BusinessStaff related theme.

```html
<!DOCTYPE html>
<html lang="en">
<head>
<meta charset="utf-8">
<title>Resume Services Banner</title>
<link href="https://fonts.googleapis.com/css2?family=Arimo:wght@400;700&display=swap" rel="stylesheet">
<style>
  :root {
    --blue-top: #3a78c8;
    --blue-mid: #1f56a8;
    --blue-deep: #123f86;
    --white: #ffffff;
    --green: #7ed321;
    --yellow: #ffee1a;
    --black: #0d0d0d;
    --photo-light: #c9c3bc;
    --photo-dark: #4a5a72;
  }
  html, body {
    margin: 0;
    padding: 0;
    width: 1200px;
    height: 148px;
    overflow: hidden;
    background: #ffffff;
  }
  .banner {
    position: relative;
    width: 1200px;
    height: 148px;
    overflow: hidden;
    font-family: "Arimo", Arial, sans-serif;
    background: linear-gradient(180deg, var(--blue-top) 0%, var(--blue-mid) 45%, var(--blue-deep) 100%);
  }
  .headline {
    position: absolute;
    left: 12px;
    top: 2px;
    margin: 0;
    font-size: 28px;
    font-weight: 400;
    color: var(--white);
    white-space: nowrap;
    letter-spacing: 0.2px;
  }
  .headline .accent {
    color: var(--green);
    font-size: 36px;
  }
  .pitch {
    position: absolute;
    margin: 0;
    font-size: 31px;
    font-weight: 400;
    color: var(--yellow);
    white-space: nowrap;
  }
  .pitch--first { left: 18px; top: 52px; }
  .pitch--second { left: 210px; top: 96px; }
  .cta {
    position: absolute;
    left: 608px;
    top: 102px;
    width: 182px;
    height: 46px;
  }
  .cta svg { position: absolute; inset: 0; }
  .cta span {
    position: absolute;
    inset: 0;
    display: flex;
    align-items: center;
    justify-content: center;
    color: var(--white);
    font-size: 22px;
  }
  .photo-frame {
    position: absolute;
    left: 788px;
    top: -135px;
    width: 418px;
    height: 418px;
    border-radius: 50%;
    box-sizing: border-box;
    border: 8px solid var(--white);
    overflow: hidden;
  }
  .photo {
    width: 100%;
    height: 100%;
    background: linear-gradient(100deg, var(--photo-light) 0%, #9aa3ae 45%, var(--photo-dark) 75%, #d8d3cc 100%);
  }
  .samples {
    position: absolute;
    left: 806px;
    top: 82px;
    width: 394px;
    height: 46px;
    background: rgba(13, 13, 13, 0.82);
    color: var(--white);
    font-size: 27px;
    display: flex;
    align-items: center;
    justify-content: center;
    white-space: nowrap;
  }
</style>
</head>
<body>
  <div class="banner">
    <h1 class="headline">How Good is Your <span class="accent">Resume</span>? Ask a Professional !</h1>
    <p class="pitch pitch--first">Get a Great Resume That will</p>
    <p class="pitch pitch--second">sharpen up your image</p>

    <a class="cta" href="#">
      <svg width="182" height="46" viewBox="0 0 182 46" aria-hidden="true">
        <polygon points="14,0 182,0 168,46 0,46" fill="#0d0d0d"/>
      </svg>
      <span>Click Here</span>
    </a>

    <div class="photo-frame">
      <div class="photo" role="img" aria-label="Office scene of a businesswoman meeting a job candidate"></div>
    </div>
    <div class="samples">Free Resume Samples</div>
  </div>
</body>
</html>
```